New Innovative Counselling and psychotherapy Service needs Business Card design

Keep it simple and professional. On one side, just company name and logo (perhaps in all blue) and maybe a tag line.

On other side (all white) my name and Qualifications in centre

Industry/Entity Type

Health And Wellness

Contact Information for Business Card

Derek Hollis
Counsellor & Psychotherapist
BSc (Psychol.), BA, Dip. (Couns. & Psych.), PG.Cert (CBT), MGVrA, NWTF

I will also require Mobile no, Email and web site address of which I'll pass on to final designer.

Font styles to use
Sans Serif

Requirements
Must have
• My Logo Only and please use the colours in logo that is in it.
Should not have
• Any other images

```html
<!DOCTYPE html>
<html lang="en">
<head>
<meta charset="utf-8">
<title>ClearHaven Business Card</title>
<link rel="stylesheet" href="https://fonts.googleapis.com/css2?family=Work+Sans:wght@400;500&display=swap">
<style>
  :root {
    --backdrop: #161616;
    --card: #303030;
    --blue: #4bb0e3;
    --green: #8cc653;
    --text: #f2f2f2;
  }
  * { margin: 0; padding: 0; box-sizing: border-box; }
  html, body {
    width: 1200px; height: 897px; overflow: hidden;
    background: var(--backdrop);
    font-family: "Work Sans", Arial, sans-serif;
    color: var(--text);
  }
  .card {
    position: absolute; left: 326px; width: 543px; height: 310px;
    background: var(--card); border-radius: 18px;
  }
  .card--front { top: 127px; }
  .card--back { top: 474px; }

  .brand {
    position: absolute; left: 42px; top: 136px;
    display: flex; align-items: center; gap: 12px;
  }
  .brand__dot { width: 36px; height: 36px; border-radius: 50%; background: var(--blue); }
  .brand__name { font-size: 22px; font-weight: 400; color: var(--text); letter-spacing: 0.2px; }

  .divider {
    position: absolute; left: 277px; top: 75px; width: 2px; height: 160px;
    background: var(--green);
  }
  .details { position: absolute; left: 297px; top: 70px; }
  .details__name {
    font-size: 26px; font-weight: 500; color: var(--blue);
    line-height: 30px; letter-spacing: 0.2px;
  }
  .details__role, .details__quals { font-size: 13.6px; line-height: 17.5px; }
  .contacts { list-style: none; margin-top: 12px; }
  .contacts li {
    display: flex; align-items: center; gap: 8px;
    font-size: 13.6px; line-height: 20px;
  }
  .contacts svg { width: 9px; height: 9px; flex: none; }
  .url-host { color: var(--green); }

  .back-brand {
    position: absolute; left: 0; right: 0; top: 112px;
    display: flex; justify-content: center; align-items: center; gap: 14px;
  }
  .back-brand .brand__dot { width: 44px; height: 44px; }
  .back-brand .brand__name { font-size: 30px; }
  .back-url {
    position: absolute; left: 0; right: 0; top: 272px;
    text-align: center; font-size: 13.6px;
  }
</style>
</head>
<body>
  <section class="card card--front">
    <div class="brand">
      <span class="brand__dot"></span>
      <span class="brand__name">ClearHaven</span>
    </div>
    <div class="divider"></div>
    <div class="details">
      <h1 class="details__name">DEREK HOLLIS</h1>
      <p class="details__role">Counsellor &amp; Psychotherapist</p>
      <p class="details__quals">BSc (Psychol.), BA, Dip.<br>(Couns. &amp; Psych.), PG.Cert<br>(CBT), MGVrA, NWTF</p>
      <ul class="contacts">
        <li>
          <svg viewBox="0 0 10 10"><path d="M2 1 L4 1 L4.6 3 L3.5 3.8 Q4.5 5.8 6.2 6.5 L7 5.4 L9 6 L9 8 Q9 9 8 9 Q1 8.5 1 2 Q1 1 2 1Z" fill="var(--blue)"/></svg>
          <span>888-555-0147</span>
        </li>
        <li>
          <svg viewBox="0 0 10 10"><rect x="0.8" y="2" width="8.4" height="6" rx="0.8" fill="none" stroke="var(--blue)" stroke-width="1"/><path d="M1 2.5 L5 5.5 L9 2.5" fill="none" stroke="var(--blue)" stroke-width="1"/></svg>
          <span>info@clearhaven.com</span>
        </li>
        <li>
          <svg viewBox="0 0 10 10"><circle cx="5" cy="5" r="4.2" fill="none" stroke="var(--blue)" stroke-width="0.9"/><ellipse cx="5" cy="5" rx="1.8" ry="4.2" fill="none" stroke="var(--blue)" stroke-width="0.8"/><path d="M0.8 5 H9.2" stroke="var(--blue)" stroke-width="0.8"/></svg>
          <span>www.<span class="url-host">clearhaven</span>.com</span>
        </li>
      </ul>
    </div>
  </section>

  <section class="card card--back">
    <div class="back-brand">
      <span class="brand__dot"></span>
      <span class="brand__name">ClearHaven</span>
    </div>
    <p class="back-url">www.<span class="url-host">clearhaven</span>.com</p>
  </section>
</body>
</html>
```